Modern Podcast Marketing Cards - BRAVOKESTREL

Update: Do "not" include my address, there's no need for this. Please remember this project needs to promote my brand along with the my new Podcast shows tagline. So this is not a traditional business card, it has to look cool enough so people want to hold onto it and not just toss it aside. So obviously "not" an old school boring business card with a ton of business contact info/text. Needs to catch attention and drive my recipients to want to visit the website " bravokestrel.net " and/or to download and listen on the apps Wavora, Plimbo, Quorra Shelf. Plus would like to drive them to Follow on my social media channels @BRAVOKESTREL; all while making sure the the design doesn't look cluttered while not being boring.
I've re-designed the logo specifically for the new show though vs what you see when you first visit my website. So the shows logo is also attached which is found on Wavora, Plimbo app, etc. That design is to promote the three domains this brand focused on "Fueling" the followers and listeners with, regarding "Health", "Business", and "Lifestyle". If logos end up on both sides of the card, one should have the version with the three words included of Health, Business, and Lifestyle. The other side should use the blank version of the logo attached which does not have those three words under the BRAVOKESTREL logo. So I gave you two versions to work with.
**Try and work in my three domains mentioned above and/or the actual tagline for the show/my brand which is "SPARK Your Health, Business, and Lifestyle". You can break it up a little if it will stand out stronger. Remember this is more of a marketing/advertising card vs a boring traditional business card.
Just to note, my profession behind the Podcast Host is my consulting as a Sales, Marketing, and Business Development consultant, But the final design should really show off my Tagline and those three domains to "SPARK Your Health, Business, and Lifestyle!" (without being cluttered)
- again I like it when the flames get ghosted or used as a transparent backdrop. Or you can somehow take a podcast microphone and overlay my logo's flames to wrap around the microphone or have the microphone stand out with "fire fueling it".
Why the three domains focus?
1. Health: because I'm a health nut, adrenaline junkie sports participant, GritLoop coach, and I have a part time nutritional business.
2. Business: because I'm a business consultant specializing in online branding and social media marketing, with 20 years of business experience.
3. Lifestyle: because I do a lot of coaching on life balance, motivational speaking, love to travel, and am always promoting people to balance their lifestyle between business, personal, and fun.

Target Market(s)

Podcasting, Online Branding & Marketing

Industry/Entity Type

Marketing

Contact Information for Business Card

More of a marketing card than a traditional business card, Double-sided, rich bold colors used from my logo's colors. Will consider the clear plastic style too.

Font styles to use
Serif
Sans Serif

Requirements
Must have
• - Drive people to want to visit the website and download/listen to my podcast via the three apps.
• - So use those apps logos somehow from Wavora Podcast app, Plimbo Radio app, and the Quorra Shelf app logos.
• - For contact info: My Name, Titles are Chief Intrepid Officer, also include Podcaster for the 2nd title. Contact info should be 1st my email, 2nd my website address without the www; and third my phone.
• Note: reduce clutter and make sure it's not too busy. That's why I'm considering a 2 sided design.
Nice to have
• - Colors should coincide with my logo and primary colors from the logos.
• - Not too much white, at least side should be a gray or blue backdrop
• - I love the style where you take the flames from my logo and ghost or make them transparent on the backdrop for the background on the card.
• - A podcast microphone logo included somehow or set it one fire with my fire from my logo would be cool.
Should not have
• - Do not list my address
• - No single sided cards
• - No crazy stripes or swoosh marks, emphasis is the FIRE so motivate people, and inspire, "to fire them up" with your design.

```html
<!DOCTYPE html>
<html lang="en">
<head>
<meta charset="utf-8">
<title>BRAVOKESTREL – Podcast Marketing Cards</title>
<link rel="stylesheet" href="https://fonts.googleapis.com/css2?family=Oswald:wght@500;700&family=Open+Sans:wght@400;600;700&display=swap">
<style>
  :root {
    --stage: #2a2a2c;
    --ink-black: #0b0b0d;
    --navy: #1d2747;
    --navy-deep: #121a33;
    --slate: #56658e;
    --paper: #ffffff;
    --ghost: #dfe2e8;
    --white: #ffffff;
    --muted-line: #8c93a8;
    --badge: #9a9ea8;
  }
  * { box-sizing: border-box; margin: 0; padding: 0; }
  html, body { width: 1200px; height: 798px; overflow: hidden; background: var(--stage); }
  .canvas { position: relative; width: 1200px; height: 798px; }

  .card { position: absolute; overflow: hidden; box-shadow: 0 10px 30px rgba(0,0,0,.45); }

  /* Front card (portrait, dark) */
  .card-front {
    left: 70px; top: 102px; width: 340px; height: 595px;
    background: linear-gradient(90deg, var(--navy-deep) 0 36%, var(--ink-black) 36% 100%);
  }
  .card-front .ghost-flame {
    position: absolute; left: 40px; top: 190px; width: 300px; height: 405px;
    background: radial-gradient(ellipse at 55% 50%, rgba(60,75,120,.6), rgba(30,38,66,.3) 55%, transparent 78%);
  }
  .front-brand { position: absolute; left: 32px; top: 118px; color: var(--white); }
  .front-brand .wordmark {
    font-family: "Oswald", sans-serif; font-weight: 700; font-size: 42px; letter-spacing: 1px; line-height: 1;
  }
  .front-brand .domains {
    margin-top: 8px; font-family: "Oswald", sans-serif; font-weight: 500; font-size: 13.5px; letter-spacing: 3px;
  }
  .front-contact {
    position: absolute; left: 150px; right: 14px; top: 420px; color: var(--white);
    font-family: "Open Sans", sans-serif; text-align: center; line-height: 1.3;
  }
  .front-contact .name { font-weight: 700; font-size: 17px; letter-spacing: .5px; }
  .front-contact .title { font-size: 14px; }
  .front-contact .details { margin-top: 14px; font-size: 14px; }

  /* Back card (landscape, white) */
  .card-back {
    left: 470px; top: 229px; width: 595px; height: 340px; background: var(--paper);
  }
  .card-back .ghost-flame {
    position: absolute; right: -20px; bottom: -20px; width: 360px; height: 230px;
    background: radial-gradient(ellipse at 60% 60%, var(--ghost), rgba(223,226,232,.55) 50%, transparent 75%);
  }
  .back-brand {
    position: absolute; left: 0; right: 0; top: 78px;
    display: flex; justify-content: center; align-items: center; gap: 14px;
  }
  .back-brand .dot { width: 56px; height: 56px; border-radius: 50%; background: var(--navy); }
  .back-brand .wordmark {
    font-family: "Oswald", sans-serif; font-weight: 700; font-size: 54px; line-height: 1; color: var(--navy);
    letter-spacing: 1px;
  }
  .handle {
    position: absolute; left: 0; right: 0; top: 166px; text-align: center;
    font-family: "Oswald", sans-serif; font-weight: 500; font-size: 13px; color: var(--navy); letter-spacing: 1px;
  }
  .rule { position: absolute; left: 40px; right: 40px; top: 192px; height: 1px; background: var(--muted-line); }
  .app-plimbo {
    position: absolute; left: 40px; top: 162px; display: flex; align-items: center; gap: 6px;
    font-family: "Oswald", sans-serif; font-weight: 700; font-size: 15px; color: var(--navy); letter-spacing: 1px;
  }
  .app-plimbo .mark { width: 14px; height: 14px; background: var(--navy); }
  .app-badge {
    position: absolute; right: 40px; top: 156px; width: 90px; height: 28px; border-radius: 5px; background: var(--badge);
  }
  .social-row {
    position: absolute; left: 0; right: 0; top: 210px; display: flex; justify-content: center; gap: 9px;
  }
  .social-row span { width: 22px; height: 22px; border-radius: 50%; background: var(--slate); }
</style>
</head>
<body>
<main class="canvas">

  <section class="card card-front" aria-label="Card front">
    <div class="ghost-flame" role="img" aria-label="Ghosted flame artwork from the logo as a dark transparent backdrop"></div>
    <div class="front-brand">
      <div class="wordmark">BRAVOKESTREL</div>
      <div class="domains">HEALTH | BUSINESS | LIFESTYLE</div>
    </div>
    <div class="front-contact">
      <div class="name">DORIAN VELCAMP</div>
      <div class="title">Chief Intrepid Officer</div>
      <div class="title">Podcaster</div>
      <div class="details">
        <div>dorian@bravokestrel.net</div>
        <div>bravokestrel.net</div>
        <div>555-014-2786</div>
      </div>
    </div>
  </section>

  <section class="card card-back" aria-label="Card back">
    <div class="ghost-flame" role="img" aria-label="Faint ghosted flame artwork as a light transparent backdrop"></div>
    <div class="back-brand">
      <span class="dot"></span>
      <span class="wordmark">BRAVOKESTREL</span>
    </div>
    <div class="app-plimbo"><span class="mark"></span>PLIMBO</div>
    <div class="handle">@BRAVOKESTREL</div>
    <div class="app-badge" aria-label="Wavora listing badge"></div>
    <div class="rule"></div>
    <div class="social-row" aria-label="Social channels">
      <span></span><span></span><span></span><span></span><span></span><span></span><span></span><span></span><span></span>
    </div>
  </section>

</main>
</body>
</html>
```